Business Card Design Project

I want my business cards to stand and feel timeless! I also want people to get their hands on them and freak out over how cool these are, I already have a logo i just want a very cool card design! this is for a makeup artist and maybe one day a line of cosmetics.

Target Market(s)

I want this to target women from 18 to 45

Industry/Entity Type

Business

Font styles to use
Decorative
Script

Colors

Designer to choose colors to be used in the design.

Requirements
Must have
• it must be elegante

```html
<!DOCTYPE html>
<html lang="en">
<head>
<meta charset="UTF-8">
<title>Rosaline – Business Card</title>
<link rel="stylesheet" href="https://fonts.googleapis.com/css2?family=Montserrat:wght@300;700&family=Pacifico&display=swap">
<style>
  :root {
    --backdrop: #1c1c1e;
    --front-base: #c9cacc;
    --front-light: #d4d5d7;
    --front-shade: #bdbec0;
    --sky: #b5d9ee;
    --ink: #1d1d1f;
    --paper: #f7f7f7;
    --charcoal: #262627;
    --charcoal-light: #3a3b3d;
    --charcoal-dark: #1f1f20;
    --accent: #1d7bb8;
    --white: #ffffff;
  }
  * { margin: 0; padding: 0; box-sizing: border-box; }
  html, body {
    width: 1200px;
    height: 800px;
    overflow: hidden;
    background: var(--backdrop);
  }
  .stage {
    position: relative;
    width: 1200px;
    height: 800px;
  }
  .card {
    position: absolute;
    width: 520px;
    height: 300px;
    display: block;
    box-shadow: 0 10px 30px rgba(0,0,0,0.45);
  }
  .card--front { left: 110px; top: 90px; }
  .card--back  { left: 570px; top: 410px; }

  .front-base { fill: var(--front-base); }
  .front-light { fill: var(--front-light); }
  .front-shade { fill: var(--front-shade); }
  .sky { fill: var(--sky); }

  .brand {
    font-family: 'Montserrat', sans-serif;
    font-weight: 300;
    fill: var(--ink);
  }
  .brand--front { font-size: 50px; letter-spacing: 9px; }
  .brand--back  { font-size: 32px; letter-spacing: 6px; }

  .back-paper { fill: var(--paper); }
  .back-dark { fill: var(--charcoal); }
  .back-dark-light { fill: var(--charcoal-light); }
  .back-dark-deep { fill: var(--charcoal-dark); }
  .accent { fill: var(--accent); }

  .person-name {
    font-family: 'Pacifico', cursive;
    font-size: 26px;
  }
  .person-name .given { fill: var(--white); }
  .person-name .family { fill: var(--accent); }
  .person-role {
    font-family: 'Pacifico', cursive;
    font-size: 15px;
    fill: var(--accent);
  }
  .contact {
    font-family: 'Montserrat', sans-serif;
    font-weight: 700;
    font-size: 16px;
    letter-spacing: 1px;
    fill: var(--white);
  }
  .icon-line { fill: none; stroke: var(--accent); stroke-width: 1.6; }
  .icon-fill { fill: var(--accent); }
</style>
</head>
<body>
<main class="stage">

  <!-- Front of card -->
  <svg class="card card--front" viewBox="0 0 520 300" aria-label="Card front">
    <rect class="front-base" width="520" height="300"/>
    <polygon class="front-light" points="70,0 520,0 520,40 300,300 210,300"/>
    <polygon class="front-shade" points="300,300 520,40 520,300" opacity="0.6"/>
    <polygon class="front-light" points="0,300 0,120 180,300" opacity="0.7"/>
    <polygon class="sky" points="40,0 95,0 40,60"/>
    <polygon class="sky" points="0,225 0,300 75,300"/>
    <text class="brand brand--front" x="260" y="168" text-anchor="middle">ROSALINE</text>
  </svg>

  <!-- Back of card -->
  <svg class="card card--back" viewBox="0 0 520 300" aria-label="Card back">
    <rect class="back-dark" width="520" height="300"/>
    <polygon class="back-dark-light" points="190,0 520,0 520,150"/>
    <polygon class="back-dark-deep" points="160,300 520,150 520,300"/>
    <polygon class="back-paper" points="0,0 190,0 160,300 0,300"/>
    <polygon class="accent" points="160,0 205,0 186,40"/>
    <polygon class="accent" points="0,240 0,300 65,300"/>
    <text class="brand brand--back" text-anchor="middle" transform="translate(112 150) rotate(-90)">ROSALINE</text>

    <text class="person-name" x="240" y="110"><tspan class="given">Clara</tspan> <tspan class="family">Hensley</tspan></text>
    <text class="person-role" x="240" y="138">CEO</text>

    <rect class="icon-line" x="242" y="166" width="9" height="15" rx="1.5"/>
    <line class="icon-line" x1="245" y1="178" x2="248" y2="178"/>
    <text class="contact" x="265" y="180">00 987 654 321</text>

    <circle class="icon-fill" cx="247" cy="209" r="6"/>
    <text class="contact" x="265" y="215">www.hensley.com</text>
  </svg>

</main>
</body>
</html>
```